Personal Development Model Graphic

I am creating a Personal Development/Coaching business and website and need some assistance with the development of a graphic that represents my methodology. I have already done what I consider to be a working version, but now it's time to have a professional design eye take a look at it and improve.

Specifically, I need assistance on color usage. I'd like each of the 8 areas of the model to have a color, and I've tried to utilize colors I feel are representative of the specific area(for example, purple for spirituality) but it doesn't really work for everything and perhaps additional thought could be put to that aspect of it.

Also, the model needs to work in reverse of the way it's pictured in the attached JPEG. So Friends needs to be first (top center)and then going clockwise, Spirituality needs to be in the 1:00 position not the 11:00 position and then continue around to Community, Family, Exercise, Career, Art/Creativity, and last at 11:00 Sexuality. I was going to update it before uploading, but I'm having trouble with Photoshop and just decided to pull the trigger on having a designer do it.

Thank you in advance for your creativity and ideas!

Industry/Entity Type

Business

Requirements
Nice to have
• It would be fantastic if it could feel modern, and high tech. I realize this is difficult with circles! But whatever you can do.

On color usage, it would again be wonderful to have colors that are more modern than traditional. I'll leave that to your discretion.

```html
<!DOCTYPE html>
<html lang="en">
<head>
<meta charset="utf-8">
<title>Happiness Model – Eight Areas of Life</title>
<link rel="stylesheet" href="https://fonts.googleapis.com/css2?family=Oswald:wght@500;600&display=swap">
<style>
  :root {
    --bg: #ffffff;
    --ring: #d9d9d9;
    --ring-light: #ffffff;
    --label: #ffffff;
    --happiness: #0aa6db;
    --friends: #8a4608;
    --spirituality: #7a2392;
    --community: #00964c;
    --family: #ff5e0c;
    --exercise: #f29410;
    --career: #0b3fcc;
    --creativity: #c20d0d;
    --sexuality: #d0147c;
  }
  html, body {
    margin: 0;
    padding: 0;
    width: 1200px;
    height: 1000px;
    overflow: hidden;
    background: var(--bg);
  }
  .model {
    display: block;
    width: 1200px;
    height: 1000px;
  }
  .area-label, .core-label {
    font-family: "Oswald", "Arial Narrow", sans-serif;
    font-weight: 600;
    fill: var(--label);
    fill-opacity: 0.92;
    text-anchor: middle;
    dominant-baseline: central;
    paint-order: stroke;
    stroke: rgba(0,0,0,0.18);
    stroke-width: 2px;
  }
  .area-label { font-size: 52px; }
  .core-label { font-size: 112px; }
  .ring-track { fill: none; stroke: var(--ring); stroke-width: 24; }
  .ring-shine { fill: none; stroke: var(--ring-light); stroke-width: 10; opacity: 0.8; }
  .area--friends { --c: var(--friends); }
  .area--spirituality { --c: var(--spirituality); }
  .area--community { --c: var(--community); }
  .area--family { --c: var(--family); }
  .area--exercise { --c: var(--exercise); }
  .area--career { --c: var(--career); }
  .area--creativity { --c: var(--creativity); }
  .area--sexuality { --c: var(--sexuality); }
  .area--core { --c: var(--happiness); }
  .sphere-base, .flow-arrow { fill: var(--c); }
</style>
</head>
<body>
<svg class="model" viewBox="0 0 1200 1000" xmlns="http://www.w3.org/2000/svg" role="img" aria-label="Happiness at the centre, fed by Friends, Spirituality, Community, Family, Exercise, Career, Art/Creativity and Sexuality">
  <defs>
    <radialGradient id="sphere-shade" cx="45%" cy="40%" r="62%">
      <stop offset="0.55" stop-color="#000" stop-opacity="0"/>
      <stop offset="1" stop-color="#000" stop-opacity="0.35"/>
    </radialGradient>
    <radialGradient id="sphere-highlight" cx="30%" cy="22%" r="45%">
      <stop offset="0" stop-color="#fff" stop-opacity="0.5"/>
      <stop offset="1" stop-color="#fff" stop-opacity="0"/>
    </radialGradient>
    <linearGradient id="sphere-gloss" x1="0" y1="0" x2="0" y2="1">
      <stop offset="0" stop-color="#fff" stop-opacity="0.22"/>
      <stop offset="1" stop-color="#fff" stop-opacity="0"/>
    </linearGradient>
    <path id="inward-arrow" d="M-8,-22 H8 V-4 L20,-10 L0,22 L-20,-10 L-8,-4 Z"/>
  </defs>

  <g class="ring">
    <circle class="ring-track" cx="600" cy="497" r="357"/>
    <circle class="ring-shine" cx="600" cy="494" r="357"/>
  </g>

  <g class="flow-arrows">
    <use href="#inward-arrow" class="flow-arrow area--friends" transform="translate(600 277) rotate(0)"/>
    <use href="#inward-arrow" class="flow-arrow area--spirituality" transform="translate(756 341) rotate(45)"/>
    <use href="#inward-arrow" class="flow-arrow area--community" transform="translate(820 497) rotate(90)"/>
    <use href="#inward-arrow" class="flow-arrow area--family" transform="translate(756 653) rotate(135)"/>
    <use href="#inward-arrow" class="flow-arrow area--exercise" transform="translate(600 717) rotate(180)"/>
    <use href="#inward-arrow" class="flow-arrow area--career" transform="translate(444 653) rotate(225)"/>
    <use href="#inward-arrow" class="flow-arrow area--creativity" transform="translate(380 497) rotate(270)"/>
    <use href="#inward-arrow" class="flow-arrow area--sexuality" transform="translate(444 341) rotate(315)"/>
  </g>

  <g class="area area--core">
    <circle class="sphere-base" cx="600" cy="497" r="190"/>
    <circle cx="600" cy="497" r="190" fill="url(#sphere-shade)"/>
    <circle cx="600" cy="497" r="190" fill="url(#sphere-highlight)"/>
    <path d="M430,450 A190,190 0 0 1 770,450 Q600,400 430,450 Z" fill="url(#sphere-gloss)"/>
    <text class="core-label" x="600" y="497" textLength="312" lengthAdjust="spacingAndGlyphs">HAPPINESS</text>
  </g>

  <g class="area area--friends">
    <circle class="sphere-base" cx="600" cy="140" r="108"/>
    <circle cx="600" cy="140" r="108" fill="url(#sphere-shade)"/>
    <circle cx="600" cy="140" r="108" fill="url(#sphere-highlight)"/>
    <text class="area-label" x="600" y="148" textLength="145" lengthAdjust="spacingAndGlyphs">FRIENDS</text>
  </g>
  <g class="area area--spirituality">
    <circle class="sphere-base" cx="850" cy="245" r="108"/>
    <circle cx="850" cy="245" r="108" fill="url(#sphere-shade)"/>
    <circle cx="850" cy="245" r="108" fill="url(#sphere-highlight)"/>
    <text class="area-label" x="850" y="250" textLength="196" lengthAdjust="spacingAndGlyphs">SPIRITUALITY</text>
  </g>
  <g class="area area--community">
    <circle class="sphere-base" cx="958" cy="497" r="108"/>
    <circle cx="958" cy="497" r="108" fill="url(#sphere-shade)"/>
    <circle cx="958" cy="497" r="108" fill="url(#sphere-highlight)"/>
    <text class="area-label" x="955" y="495" textLength="192" lengthAdjust="spacingAndGlyphs">COMMUNITY</text>
  </g>
  <g class="area area--family">
    <circle class="sphere-base" cx="850" cy="750" r="108"/>
    <circle cx="850" cy="750" r="108" fill="url(#sphere-shade)"/>
    <circle cx="850" cy="750" r="108" fill="url(#sphere-highlight)"/>
    <text class="area-label" x="850" y="748" textLength="128" lengthAdjust="spacingAndGlyphs">FAMILY</text>
  </g>
  <g class="area area--exercise">
    <circle class="sphere-base" cx="600" cy="855" r="108"/>
    <circle cx="600" cy="855" r="108" fill="url(#sphere-shade)"/>
    <circle cx="600" cy="855" r="108" fill="url(#sphere-highlight)"/>
    <text class="area-label" x="598" y="852" textLength="158" lengthAdjust="spacingAndGlyphs">EXERCISE</text>
  </g>
  <g class="area area--career">
    <circle class="sphere-base" cx="348" cy="750" r="108"/>
    <circle cx="348" cy="750" r="108" fill="url(#sphere-shade)"/>
    <circle cx="348" cy="750" r="108" fill="url(#sphere-highlight)"/>
    <text class="area-label" x="348" y="748" textLength="132" lengthAdjust="spacingAndGlyphs">CAREER</text>
  </g>
  <g class="area area--creativity">
    <circle class="sphere-base" cx="243" cy="497" r="108"/>
    <circle cx="243" cy="497" r="108" fill="url(#sphere-shade)"/>
    <circle cx="243" cy="497" r="108" fill="url(#sphere-highlight)"/>
    <text class="area-label" x="245" y="468" textLength="76" lengthAdjust="spacingAndGlyphs">ART/</text>
    <text class="area-label" x="245" y="522" textLength="168" lengthAdjust="spacingAndGlyphs">CREATIVITY</text>
  </g>
  <g class="area area--sexuality">
    <circle class="sphere-base" cx="348" cy="245" r="108"/>
    <circle cx="348" cy="245" r="108" fill="url(#sphere-shade)"/>
    <circle cx="348" cy="245" r="108" fill="url(#sphere-highlight)"/>
    <text class="area-label" x="346" y="250" textLength="176" lengthAdjust="spacingAndGlyphs">SEXUALITY</text>
  </g>
</svg>
</body>
</html>
```